Briefpapier für Seehafenspedition im Bereich Zollabfertigung
Zielgruppe
Seehafenspedition im Bereich Zollabfertigung (Import & Export), Hafenabfertigung und weltweiter Transport (See- und Landtransporte). Zielgruppe sind Privatkunden als auch Geschäftskunden.
Aufgabenstellung
Wir bitten um ein Design für unser Briefpapier.
Wir suchen ein hochwertiges Design, das die Werte Vertrauen, Exklusivität und Innovation ausstrahlt. Es soll edel aussehen.
Bitte für Telefon, Mail etc. Icons benutzen, damit es für jedermann verständlich ist, unabhängig von der Sprache.
Bitte orientieren Sie sich am Design unseres Logos und unserer Visitenkarten.
Die Datensätze sollten sich mit entsprechendem Programm von uns bearbeiten lassen.
Wir freuen uns schon auf die Entwürfe.
Vielen Dank im Voraus!

```html
<!DOCTYPE html>
<html lang="de">
<head>
<meta charset="utf-8">
<title>Kestrel Cargo – Briefpapier</title>
<link href="https://fonts.googleapis.com/css2?family=Roboto:wght@400;500&display=swap" rel="stylesheet">
<style>
  :root {
    --orange: #f39208;
    --grey: #6b6b6b;
    --text: #4a4a4a;
    --rule: #d9d9d9;
    --faint: #f3f3f3;
    --paper: #ffffff;
  }
  html, body { margin: 0; padding: 0; overflow: hidden; }
  body { width: 867px; height: 1200px; background: var(--paper); font-family: "Roboto", sans-serif; color: var(--text); }
  .sheet { position: relative; width: 867px; height: 1200px; overflow: hidden; background: var(--paper); }
  .band { position: absolute; left: 0; width: 867px; }
  .band--top { top: 0; height: 30px; }
  .band--bottom { bottom: 0; height: 30px; }
  .brand { position: absolute; left: 566px; top: 62px; display: flex; align-items: center; gap: 10px; }
  .brand__dot { width: 32px; height: 32px; border-radius: 50%; background: var(--orange); }
  .brand__name { font-size: 26px; font-weight: 500; letter-spacing: 3px; color: var(--grey); text-transform: uppercase; }
  .contact { position: absolute; left: 618px; top: 112px; padding-left: 10px; border-left: 1px solid #9a9a9a; font-size: 11px; line-height: 13px; width: 230px; }
  .contact__company { position: relative; font-size: 13px; line-height: 16px; color: var(--grey); }
  .contact__company::before { content: ""; position: absolute; left: -21px; top: 3px; border-left: 5px solid var(--orange); border-top: 5px solid transparent; border-bottom: 5px solid transparent; }
  .contact p { margin: 0; }
  .contact__group { margin-top: 13px; }
  .contact__label { color: var(--orange); }
  .contact__icon-line { display: flex; align-items: center; gap: 5px; font-size: 12px; line-height: 15px; }
  .contact__icon-line svg { width: 9px; height: 9px; fill: var(--orange); }
  .address-window { position: absolute; left: 84px; top: 161px; width: 370px; height: 185px; border: 1px solid #ececec; border-radius: 24px; box-sizing: border-box; }
  .address-window__inner { position: absolute; left: 14px; top: 14px; right: 14px; bottom: 14px; border: 1px dashed #dcdcdc; border-radius: 14px; }
  .sender-line { position: absolute; left: 137px; top: 181px; font-size: 9px; padding-bottom: 2px; border-bottom: 1px solid var(--grey); color: var(--text); }
  .sender-line span { color: var(--orange); }
  .fold-mark { position: absolute; left: 5px; width: 0; height: 0; border-left: 5px solid var(--orange); border-top: 4px solid transparent; border-bottom: 4px solid transparent; }
  .fold-mark--first { top: 401px; }
  .fold-mark--second { top: 806px; }
  .backdrop-circle { position: absolute; left: 2px; top: 800px; width: 445px; height: 445px; border-radius: 50%; background: var(--faint); }
  .web { position: absolute; left: 237px; bottom: 5px; display: flex; align-items: center; gap: 6px; color: #fff; font-size: 14px; font-weight: 500; }
  .web svg { width: 14px; height: 14px; }
</style>
</head>
<body>
<div class="sheet">
  <svg class="band band--top" viewBox="0 0 867 30" aria-hidden="true">
    <polygon points="0,0 225,0 238,7 395,7 375,26 0,26" fill="var(--orange)"/>
    <polygon points="380,26 398,7 410,7 392,26" fill="var(--grey)"/>
    <polygon points="403,26 421,7 433,7 415,26" fill="var(--orange)"/>
    <polygon points="426,26 444,7 474,7 456,26" fill="var(--grey)"/>
  </svg>

  <div class="backdrop-circle" aria-hidden="true"></div>

  <div class="brand">
    <span class="brand__dot"></span>
    <span class="brand__name">Kestrel Cargo</span>
  </div>

  <div class="contact">
    <p class="contact__company">Kestrel Cargo GmbH</p>
    <p>Kaiweg 12</p>
    <p>27568 Bremerhaven</p>
    <div class="contact__group">
      <p class="contact__icon-line"><svg viewBox="0 0 10 10"><path d="M2 0h2l1 2.5-1.2 1a5 5 0 0 0 2.7 2.7l1-1.2L10 6v2a2 2 0 0 1-2 2A8 8 0 0 1 0 2 2 2 0 0 1 2 0z"/></svg>+49 471 5550312-0</p>
      <p class="contact__icon-line"><svg viewBox="0 0 10 10"><path d="M0 2h10v7H0z M0 2l5 4 5-4" stroke="#fff" stroke-width="0.8"/></svg>info@kestrelcargo.de</p>
    </div>
    <div class="contact__group">
      <p class="contact__label">Bremerhaven:</p>
      <p>Register: HRB 40917 HB;</p>
      <p>USt-IdNr. / VAT-No.: DE418260517;</p>
      <p>Geschäftsführer / CEO: Holger Brandtner</p>
    </div>
    <div class="contact__group">
      <p class="contact__label">Nordhafen Bank</p>
      <p>IBAN: DE12 3456 0078 0123 4567 00</p>
      <p>BIC: NRDHDEFFXXX</p>
    </div>
  </div>

  <div class="address-window"><div class="address-window__inner"></div></div>
  <p class="sender-line" style="margin:0">Kestrel Cargo GmbH <span>|</span> Kaiweg 12 <span>|</span> 27568 Bremerhaven</p>

  <div class="fold-mark fold-mark--first"></div>
  <div class="fold-mark fold-mark--second"></div>

  <svg class="band band--bottom" viewBox="0 0 867 30" aria-hidden="true">
    <polygon points="0,4 568,4 582,10 867,10 867,30 0,30" fill="var(--orange)"/>
    <polygon points="720,30 740,10 755,10 735,30" fill="var(--paper)"/>
    <polygon points="726,30 746,10 766,10 746,30" fill="var(--grey)"/>
    <polygon points="752,30 772,10 786,10 766,30" fill="var(--orange)"/>
    <polygon points="772,30 792,10 812,10 792,30" fill="var(--grey)"/>
    <polygon points="798,30 818,10 826,10 806,30" fill="var(--paper)"/>
  </svg>
  <div class="web">
    <svg viewBox="0 0 14 14" fill="none" stroke="#fff" stroke-width="1.2"><circle cx="7" cy="7" r="6"/><ellipse cx="7" cy="7" rx="2.6" ry="6"/><path d="M1 7h12M2 4h10M2 10h10"/></svg>
    www.kestrelcargo.de
  </div>
</div>
</body>
</html>
```